Dorian's Roam Almanac Mobile App

We need a sleek new design for our new mobile app we are launching in the South Pacific. This app will be released for both iPhone and Android. The app has already been developed and your new design will give it the finishing touch we need to release it to our audience. This will be the premiere tourism app for the South Pacific and will be advertised heavily in our successful print publications which are distributed internationally. We are looking for you to provide two designs (for two screens in our mobile app) for this competition. The selected winner will have the opportunity to design the remaining screens in our app and website as a separate contract.

Attached you will see a few of the screens that currently exist in our mobile app to give you a feel for the functionality. The two screens we want you to design for this competition are the main listing page and the category selection page. These two screens will be included in the uploaded files and will be clearly marked so you know what we are looking for.

Please feel free to reach out to us with any questions if you need any guidance in directing your designs. Show us something sleek, engaging, and ultimately something that will drive our users to want to engage with the businesses that are listed in the app.

Please see the uploaded files for a couple of our current designs, the two screens we want you to design for this competition, and a few samples of design ideas we like.

Best of Luck!

Target Market(s)

Travelers to the South Pacific

Industry/Entity Type

Travel Industry

Font styles to use
Serif
Sans Serif

Colors
0492cd
33a6d7
ec1f27
f04a50
85cae6
cee9f5
f59296
cedeed
fbd4d5

Requirements
Must have
• Clean, attractive design for the two screens mentioned in the brief.
Nice to have
• Icon sets, color guide, font selection
Should not have
• Project should not be too busy or incorporate too many different colors, styles, fonts, etc.

```html
<!DOCTYPE html>
<html lang="en">
<head>
<meta charset="utf-8">
<title>Dorian's Roam Almanac — Rarotonga</title>
<link rel="stylesheet" href="https://fonts.googleapis.com/css2?family=Lato:wght@300;400;900&display=swap">
<style>
  :root {
    --canvas: #eef1f8;
    --white: #ffffff;
    --lodging: #85609c;
    --transport: #eeaa55;
    --dining: #cf4c5e;
    --activities: #356487;
    --sea-deep: #1d3f8c;
    --sea-mid: #2a6fa6;
    --lagoon: #3cc3c9;
    --island: #2d7a5a;
  }
  * { box-sizing: border-box; margin: 0; padding: 0; }
  html, body {
    width: 667px; height: 1200px; overflow: hidden;
    background: var(--canvas);
    font-family: "Lato", sans-serif;
  }
  .screen {
    position: absolute; left: 7px; top: 16px;
    width: 654px; height: 1169px;
    overflow: hidden; background: var(--white);
  }
  .hero {
    position: relative; height: 350px;
    color: var(--white); text-align: center;
  }
  .hero-photo {
    position: absolute; inset: 0;
    background:
      radial-gradient(ellipse 60% 40% at 30% 45%, var(--island) 0%, rgba(45,122,90,0) 70%),
      radial-gradient(ellipse 70% 25% at 55% 78%, var(--lagoon) 0%, rgba(60,195,201,0) 75%),
      linear-gradient(180deg, #5aa6c4 0%, var(--sea-mid) 18%, var(--sea-deep) 45%, var(--sea-mid) 100%);
  }
  .back {
    position: absolute; left: 24px; top: 14px;
    display: flex; flex-direction: column; align-items: center;
    font-size: 14px; font-weight: 400; letter-spacing: 0.3px;
  }
  .back svg { width: 30px; height: 24px; }
  .hero-title {
    position: absolute; left: 0; right: 0; top: 158px;
  }
  .hero-title h1 {
    font-size: 47px; font-weight: 900; line-height: 1; letter-spacing: 0.2px;
  }
  .hero-title p {
    font-size: 29px; font-weight: 300; line-height: 1; margin-top: 6px;
  }
  .category {
    height: 238px; position: relative; color: var(--white); text-align: center;
  }
  .category svg {
    position: absolute; left: 50%; top: 62px;
    width: 80px; height: 80px; transform: translateX(-50%);
  }
  .category span {
    position: absolute; left: 0; right: 0; top: 138px;
    font-size: 35px; font-weight: 300;
  }
  .lodging { background: var(--lodging); }
  .transport { background: var(--transport); }
  .dining { background: var(--dining); }
  .activities { background: var(--activities); }
</style>
</head>
<body>
<main class="screen">
  <header class="hero">
    <div class="hero-photo" role="img" aria-label="Aerial view of Rarotonga's green mountains, lagoon and reef"></div>
    <div class="back">
      <svg viewBox="0 0 30 24" fill="none" stroke="currentColor" stroke-width="3" stroke-linecap="round" stroke-linejoin="round">
        <path d="M9 3 L3 9 L9 15"/><path d="M3 9 H19 a6 6 0 0 1 0 12 H10"/>
      </svg>
      BACK
    </div>
    <div class="hero-title">
      <h1>COOK ISLANDS</h1>
      <p>RAROTONGA</p>
    </div>
  </header>

  <section class="category lodging">
    <svg viewBox="0 0 100 100" fill="var(--white)">
      <path d="M4 46 L50 6 L96 46" fill="none" stroke="var(--white)" stroke-width="9" stroke-linecap="round" stroke-linejoin="round"/>
      <rect x="70" y="12" width="10" height="20"/>
      <path d="M18 48 L50 20 L82 48 V96 H56 V70 H44 V96 H18 Z"/>
      <rect x="58" y="56" width="12" height="12" fill="var(--lodging)"/>
    </svg>
    <span>Accomodations</span>
  </section>

  <section class="category transport">
    <svg viewBox="0 0 100 100" fill="var(--white)">
      <rect x="38" y="8" width="24" height="12" rx="3"/>
      <path d="M26 22 H74 L88 52 V80 H12 V52 Z"/>
      <path d="M32 30 H68 L77 50 H23 Z" fill="var(--transport)"/>
      <circle cx="27" cy="63" r="7" fill="var(--transport)"/>
      <circle cx="73" cy="63" r="7" fill="var(--transport)"/>
      <rect x="14" y="76" width="18" height="18" rx="6"/>
      <rect x="68" y="76" width="18" height="18" rx="6"/>
    </svg>
    <span>Transportation</span>
  </section>

  <section class="category dining">
    <svg viewBox="0 0 100 100" fill="none" stroke="var(--white)" stroke-linecap="round" stroke-linejoin="round">
      <path d="M10 6 C4 26 18 44 36 54 L80 94" stroke-width="12"/>
      <path d="M10 6 L40 46" stroke-width="12"/>
      <path d="M20 92 L66 42" stroke-width="12"/>
      <path d="M66 42 L58 30 L80 8 M66 42 L78 50 L98 28 M70 24 L84 38" stroke-width="8"/>
    </svg>
    <span>Food/Drink</span>
  </section>

  <section class="category activities">
    <svg viewBox="0 0 100 100" fill="none" stroke="var(--white)" stroke-width="7" stroke-linecap="round" stroke-linejoin="round" style="top:65px">
      <circle cx="22" cy="68" r="18"/>
      <circle cx="78" cy="68" r="18"/>
      <path d="M22 68 L38 36 H70 L78 68 M38 36 L52 68 L70 36 M66 20 L72 36 M58 20 H74 M34 28 H46"/>
    </svg>
  </section>
</main>
</body>
</html>
```